Web site design for Brivolt Software (www.brivoltsoftware-example.com)

Need the design as well as the html for the website. The brief is given in the attached file.
If possible, would like to use pencil sketches instead of images to give a unique look to the site.
Target Market(s)
small Software product companies
Industry/Entity Type
Software
Coding
Coded - Design and coding required
Number of Pages Required
5+ page

```html
<!DOCTYPE html>
<html lang="en">
<head>
<meta charset="utf-8">
<title>Brivolt Software</title>
<link rel="stylesheet" href="https://fonts.googleapis.com/css2?family=Raleway:wght@400;600;700;800&family=Open+Sans:wght@400;600&display=swap">
<style>
:root{
  --red:#e2161c;
  --red-dark:#b50f14;
  --ink:#2b2b2b;
  --grey-text:#6d6d6d;
  --hero-bg:#ececec;
  --dark:#262626;
  --testi-bg:#c4c4c4;
  --footer:#0e0e0e;
  --white:#ffffff;
}
*{box-sizing:border-box;margin:0;padding:0}
html,body{width:773px;height:1200px;overflow:hidden}
body{font-family:"Open Sans",Arial,sans-serif;color:var(--ink);background:var(--white);position:relative}

/* header */
.site-header{position:absolute;left:0;top:0;width:773px;height:78px;background:var(--white);border-bottom:1px solid #e3e3e3}
.brand{position:absolute;left:77px;top:16px;font-family:"Raleway",sans-serif;font-weight:800;font-size:17px;letter-spacing:3px;color:var(--ink)}
.top-social{position:absolute;right:95px;top:18px;display:flex;gap:5px}
.top-social span{width:8px;height:8px;background:var(--red)}
.main-nav{position:absolute;right:62px;top:52px;display:flex;align-items:center;white-space:nowrap}
.main-nav a{font-family:"Raleway",sans-serif;font-size:8px;font-weight:600;color:#444;text-decoration:none;padding:0 8px;border-right:1px solid #ddd;line-height:11px}
.main-nav a:last-of-type{border-right:none}
.search-btn{width:22px;height:22px;background:var(--red);margin-left:6px;display:flex;align-items:center;justify-content:center}

/* hero */
.hero{position:absolute;left:0;top:78px;width:773px;height:250px;background:var(--hero-bg);overflow:hidden}
.hero-photo{position:absolute;right:0;top:0;width:470px;height:250px;background:linear-gradient(120deg,#f4f4f4 0%,#dcdcdc 55%,#c8c8c8 100%)}
.hero-shapes{position:absolute;left:0;top:0}
.hero-title{position:absolute;left:77px;top:58px;font-family:"Raleway",sans-serif;font-weight:800;font-size:28px;color:var(--red);white-space:nowrap}
.hero-sub{position:absolute;left:77px;top:94px;font-family:"Raleway",sans-serif;font-weight:600;font-size:17px;color:var(--ink);white-space:nowrap}
.hero-text{position:absolute;left:77px;top:122px;width:250px;font-size:9.5px;line-height:13px;color:var(--grey-text)}
.btn{display:inline-block;background:var(--red);color:var(--white);font-family:"Raleway",sans-serif;font-weight:700;font-size:9px;padding:7px 12px;letter-spacing:.5px}
.hero .btn{position:absolute;left:77px;top:160px}

/* service cards */
.services{position:absolute;left:0;top:328px;width:773px;height:180px;background:var(--white)}
.cards{position:absolute;left:77px;top:0;display:flex;gap:8px}
.card{width:147px;height:165px;background:var(--red);color:var(--white);text-align:center;padding-top:14px}
.card svg{display:block;margin:0 auto 8px}
.card h3{font-family:"Raleway",sans-serif;font-size:12px;font-weight:700;line-height:15px;height:32px}
.card p{font-size:8.5px;line-height:12px;padding:6px 16px 0;height:46px}
.card .more{font-family:"Raleway",sans-serif;font-size:8.5px;font-weight:700;margin-top:8px}

/* passionate */
.passion{position:absolute;left:0;top:508px;width:773px;height:172px;background:var(--dark);overflow:hidden;text-align:center;color:var(--white)}
.passion h2{position:relative;font-family:"Raleway",sans-serif;font-size:19px;font-weight:700;letter-spacing:1px;margin-top:28px}
.passion p{position:relative;width:400px;margin:14px auto 0;font-size:9px;line-height:14px;color:#cfcfcf}
.passion .btn{position:relative;margin-top:14px}

/* testimonials */
.testimonials{position:absolute;left:0;top:680px;width:773px;height:275px;background:linear-gradient(180deg,#cfcfcf,#b9b9b9);text-align:center}
.testimonials h2{font-family:"Raleway",sans-serif;font-size:19px;font-weight:700;color:var(--ink);margin-top:26px;letter-spacing:1px}
.avatar{width:58px;height:58px;border-radius:50%;margin:14px auto 0;background:radial-gradient(circle at 50% 40%,#8a8a8a,#4a4a4a);border:3px solid var(--white)}
.quote-mark{position:absolute;font-family:"Raleway",sans-serif;font-weight:800;font-size:80px;color:#8f8f8f;line-height:1}
.quote-open{left:125px;top:100px}
.quote-close{right:125px;top:190px}
.testimonials blockquote{width:430px;margin:16px auto 0;font-size:9px;line-height:15px;color:#3d3d3d}
.client-name{font-family:"Raleway",sans-serif;font-weight:700;font-size:10px;margin-top:12px;color:var(--ink)}

/* footer */
.site-footer{position:absolute;left:0;top:955px;width:773px;height:245px;background:var(--footer);color:#bdbdbd}
.foot-nav{display:flex;justify-content:center;padding-top:22px;border-bottom:1px solid #2b2b2b;padding-bottom:16px;margin:0 77px;white-space:nowrap}
.foot-nav a{font-family:"Raleway",sans-serif;font-size:8px;color:#9a9a9a;text-decoration:none;padding:0 11px}
.foot-brand{position:absolute;left:77px;top:72px;font-family:"Raleway",sans-serif;font-weight:800;font-size:15px;letter-spacing:3px;color:var(--white)}
.foot-col{position:absolute;top:100px}
.foot-col h4{font-family:"Raleway",sans-serif;font-size:12px;font-weight:600;color:var(--white);margin-bottom:8px}
.foot-col p{font-size:8px;line-height:13px;color:#9a9a9a}
.col-ireland{left:77px;width:180px}
.col-india{left:290px;width:150px}
.col-news{left:470px;width:230px}
.news-form{display:flex;margin-top:4px}
.news-form .field{flex:1;height:22px;background:#2a2a2a;font-size:8px;color:#777;padding:5px 8px}
.news-form .submit{width:60px;height:22px;background:var(--red);color:var(--white);font-family:"Raleway",sans-serif;font-weight:700;font-size:9px;display:flex;align-items:center;justify-content:center}
.foot-social{display:flex;gap:6px;margin-top:12px}
.foot-social span{width:12px;height:12px;background:var(--red)}
.copyright{position:absolute;left:0;bottom:14px;width:773px;text-align:center;font-size:7px;color:#666}
</style>
</head>
<body>

<header class="site-header">
  <div class="brand">BRIVOLT</div>
  <div class="top-social"><span></span><span></span><span></span><span></span><span></span></div>
  <nav class="main-nav">
    <a href="#">HOME</a><a href="#">ABOUT US</a><a href="#">SERVICES</a><a href="#">EXPERTISE</a><a href="#">WORK WITH US</a><a href="#">CASE STUDIES</a><a href="#">DOWNLOAD</a><a href="#">CONTACT US</a>
    <span class="search-btn"><svg width="12" height="12" viewBox="0 0 12 12"><circle cx="5" cy="5" r="3.6" fill="none" stroke="#fff" stroke-width="1.6"/><line x1="7.6" y1="7.6" x2="11" y2="11" stroke="#fff" stroke-width="1.8"/></svg></span>
  </nav>
</header>

<section class="hero">
  <div class="hero-photo" role="img" aria-label="Hands typing on a laptop at a bright desk"></div>
  <svg class="hero-shapes" width="773" height="250" viewBox="0 0 773 250">
    <polygon points="0,205 360,250 0,250" fill="#e2161c"/>
    <polygon points="0,230 200,250 0,250" fill="#b50f14"/>
    <polygon points="430,250 773,170 773,250" fill="#2e2e2e"/>
  </svg>
  <div class="hero-title">WE TAKE CARE OF YOUR</div>
  <div class="hero-sub">PRODUCT'S PRESENT AND FUTURE</div>
  <p class="hero-text">You need a software product development partner for whom product development work is not just a project</p>
  <span class="btn">READ MORE</span>
</section>

<section class="services">
  <div class="cards">
    <article class="card">
      <svg width="30" height="30" viewBox="0 0 30 30" fill="#fff"><polygon points="15,3 28,10 2,10"/><rect x="5" y="12" width="3" height="11"/><rect x="11" y="12" width="3" height="11"/><rect x="17" y="12" width="3" height="11"/><rect x="23" y="12" width="3" height="11"/><rect x="2" y="24" width="26" height="3"/></svg>
      <h3>Banking &amp;<br>Financial Services</h3>
      <p>Brivolt works in the area of solutions and services for banking clients</p>
      <div class="more">MORE &gt;&gt;</div>
    </article>
    <article class="card">
      <svg width="30" height="30" viewBox="0 0 30 30" fill="none" stroke="#fff" stroke-width="2"><line x1="15" y1="11" x2="9" y2="28"/><line x1="15" y1="11" x2="21" y2="28"/><circle cx="15" cy="10" r="2" fill="#fff"/><path d="M9 5a8 8 0 0 0 0 10M21 5a8 8 0 0 1 0 10"/></svg>
      <h3>Telecom</h3>
      <p>Brivolt works on the area of solutions and services for telecom</p>
      <div class="more">MORE &gt;&gt;</div>
    </article>
    <article class="card">
      <svg width="30" height="30" viewBox="0 0 30 30" fill="none" stroke="#fff" stroke-width="2"><rect x="9" y="2" width="12" height="26" rx="2"/><line x1="13" y1="24" x2="17" y2="24"/></svg>
      <h3>Handset App<br>Development</h3>
      <p>This is developed for a complete company with expertise</p>
      <div class="more">MORE &gt;&gt;</div>
    </article>
    <article class="card">
      <svg width="30" height="30" viewBox="0 0 30 30" fill="#fff"><circle cx="9" cy="8" r="4"/><circle cx="21" cy="8" r="4"/><path d="M2 24c0-6 4-9 7-9s7 3 7 9z"/><path d="M14 24c0-6 4-9 7-9s7 3 7 9z"/></svg>
      <h3>Business<br>Consulting</h3>
      <p>Brivolt works in the area of solutions and services for industries</p>
      <div class="more">MORE &gt;&gt;</div>
    </article>
  </div>
</section>

<section class="passion">
  <svg style="position:absolute;left:0;top:0" width="773" height="172" viewBox="0 0 773 172"><polygon points="0,0 300,0 0,120" fill="#323232"/><polygon points="773,60 773,172 520,172" fill="#1c1c1c"/></svg>
  <h2>WE ARE PASSIONATE</h2>
  <p>In our belief that a software product's architecture goes a long way in avoiding costly and complex upgrades. Our architecture driven approach makes sure that product upgrades are possible while maintaining productive and friendly user interfaces.</p>
  <span class="btn">READ MORE</span>
</section>

<section class="testimonials">
  <h2>TESTIMONIALS</h2>
  <div class="avatar" role="img" aria-label="Client portrait"></div>
  <span class="quote-mark quote-open">&ldquo;</span>
  <span class="quote-mark quote-close">&rdquo;</span>
  <blockquote>Our company team has been working closely with the Brivolt team for several years. Their attention to detail and steady delivery have helped us release each product version on time and with confidence. They understand our goals and always suggest practical improvements that save real effort. We count on them for every new project.</blockquote>
  <div class="client-name">CLIENT NAME</div>
</section>

<footer class="site-footer">
  <nav class="foot-nav">
    <a href="#">HOME</a><a href="#">ABOUT US</a><a href="#">SERVICES</a><a href="#">EXPERTISE</a><a href="#">WORK WITH US</a><a href="#">CASE STUDIES</a><a href="#">DOWNLOAD</a><a href="#">CONTACT US</a>
  </nav>
  <div class="foot-brand">BRIVOLT</div>
  <div class="foot-col col-ireland">
    <h4>Ireland</h4>
    <p>Brivolt Software Ltd.<br>Unit 3, Example Court<br>Sample Road, Westbury<br>Countytown, Ireland<br>Tel: +353 00 000 0000</p>
  </div>
  <div class="foot-col col-india">
    <h4>India</h4>
    <p>Suite 2, Sample Tower<br>Example Lane, North Side<br>Citytown, India</p>
  </div>
  <div class="foot-col col-news">
    <h4>Newsletter</h4>
    <div class="news-form"><span class="field">Enter your email</span><span class="submit">SUBMIT</span></div>
    <div class="foot-social"><span></span><span></span><span></span><span></span><span></span></div>
  </div>
  <div class="copyright">&copy; BRIVOLT SOFTWARE. ALL RIGHTS RESERVED</div>
</footer>

</body>
</html>
```